Trifold for International Business Consulting firm

I have created a trifold piece (attached) that includes all the necessary information in a Word template; however, I need a professional that can make it look "current, international and modern". Our website, brenvaleadvisory.com, should give an idea as to the style and color template we like.

```html
<!DOCTYPE html>
<html lang="en">
<head>
<meta charset="utf-8">
<title>Brenvale Advisory Trifold</title>
<link rel="stylesheet" href="https://fonts.googleapis.com/css2?family=Open+Sans:wght@400;700&family=Tinos&display=swap">
<style>
  :root {
    --stage: #3b3b3b;
    --paper: #f4f5f3;
    --paper-shade: #e3e5e2;
    --olive: #b3c77a;
    --olive-dark: #9fb45f;
    --num-pale: #d9dc8e;
    --lime: #c3d33f;
    --lime-light: #d0dc5c;
    --pale-yellow: #e8e79a;
    --ink: #222222;
    --accent-text: #b9cc3e;
  }
  * { box-sizing: border-box; margin: 0; padding: 0; }
  html, body {
    width: 1200px; height: 761px; overflow: hidden;
    background: var(--stage);
    font-family: "Open Sans", sans-serif;
    color: var(--ink);
  }
  .trifold {
    position: absolute; left: 40px; top: 24px;
    width: 1120px; height: 713px;
    display: flex;
  }
  .panel { width: 373.33px; height: 100%; padding: 22px 28px; font-size: 12.4px; line-height: 1.42; }
  .panel p { margin-bottom: 4px; }
  .panel--left { background: linear-gradient(90deg, var(--paper-shade), var(--paper)); }
  .panel--middle { background: linear-gradient(90deg, var(--lime), var(--lime-light) 60%, var(--lime)); padding-top: 30px; }
  .panel--right { background: linear-gradient(90deg, var(--paper), var(--paper-shade)); }
  .section-title {
    font-weight: 400; text-transform: uppercase; letter-spacing: 0.5px;
    font-size: 17px; line-height: 1.2;
  }
  .section-title--band { background: var(--olive); padding: 6px 10px; margin: 0 -6px 10px 30px; }
  .section-title--band-wide { background: var(--olive); padding: 10px 10px; margin: 14px -6px 10px 0; font-size: 19px; }
  .section-title--plain { margin-bottom: 22px; font-size: 16px; }
  .section-title--plain-lower { margin: 16px 0 14px; font-size: 18px; }
  .section-title--pale { background: var(--pale-yellow); padding: 6px 10px; margin: 0 0 14px 0; display: inline-block; font-size: 16px; }
  .lead { font-weight: 700; }
  .question-list { list-style: none; margin: 6px 0; }
  .question-list li { margin-bottom: 5px; }
  .num {
    display: inline-block; width: 20px; height: 18px; border-radius: 50%;
    background: var(--olive-dark); font-size: 11px; text-align: center; line-height: 18px;
    margin-right: 24px;
  }
  .num--pale { background: var(--num-pale); }
  .rule { border: none; border-top: 1px solid var(--pale-yellow); margin: 8px 0; }
  .brand { display: flex; align-items: center; gap: 8px; margin: 12px 0 8px; font-size: 20px; font-weight: 700; letter-spacing: 1px; }
  .brand__mark { width: 14px; height: 14px; background: var(--ink); }
  .contact dt { color: var(--accent-text); font-weight: 700; text-transform: uppercase; font-size: 12.4px; }
  .contact dd { margin-bottom: 2px; }
  .contact .web { font-weight: 700; }
  .copyright { font-family: "Tinos", serif; font-size: 13px; }
</style>
</head>
<body>
<main class="trifold">
  <section class="panel panel--left">
    <h2 class="section-title section-title--band">Should we expand?</h2>
    <p><span class="lead">IT DEPENDS</span>: Brenvale Advisory can assist you in an initial analysis to see if your company is prepared financially to expand and if the current infrastructure is adequate for international operations. We look at human resources, technology, operations, systems, processes and do a complete SWOT analysis of your current operation.</p>
    <ol class="question-list">
      <li><span class="num num--pale">1.</span>Have you maximized your current opportunities? Is your company mature for this endeavor?</li>
      <li><span class="num">2.</span>Have you discussed with all invested parties and taken all feedback into consideration?</li>
      <li><span class="num num--pale">3.</span>What are your short, mid and long term goals for growth?</li>
    </ol>
    <p>If you are not ready for international expansion today, we will design the path to help you get there.</p>
    <h2 class="section-title section-title--band-wide">How do we expand?</h2>
    <p>One of three ways:</p>
    <ol class="question-list">
      <li><span class="num">1.</span>Green pasture-organic growth. Evolve your current business internationally, or create a new business from scratch</li>
      <li><span class="num">2.</span>Joint Venture (JV) - partner with another entity in country of expansion</li>
      <li><span class="num">3.</span>Merger or Acquisition (M&amp;A) - merge or acquire a new entity in country of expansion</li>
    </ol>
  </section>

  <section class="panel panel--middle">
    <h2 class="section-title section-title--plain">Which expansion opportunity is best for my company?</h2>
    <p>Each opportunity has its own pros and cons for growth which can be largely dependent on the country of expansion and your budget. Some countries are business friendly for new business creation and growth while others are more optimal for international businesses to join, merge or acquire established companies in country.</p>
    <p>To determine the best way forward, it is good practice to seek counsel on your different options. Our networks specialize in all categories needed for international expansion, and our consultants coordinate with each specialist to work in unison for your best interest</p>
    <h2 class="section-title section-title--plain-lower">Working with specialists</h2>
    <p>We have spent years developing relationships with accounting, legal and financial specialists’ necessary for international growth. We have business associates located on both sides of the border, positioned for cost and time efficiencies and with the expertise you need to succeed in your growth plans. Instead of parading individual groups of specialists in front of you, each with its own sales pitch and service offerings, we introduce and manage the entire relationship and service. With a single point of contact and negotiated rates for your benefit, we keep your costs at an optimal level.</p>
  </section>

  <section class="panel panel--right">
    <h2 class="section-title section-title--pale">Cultural managment</h2>
    <p>In addition to international business consulting services, we have expertise in the cultural intricacies of international business and offer Crossway Learning training. We have more than 20 years of experience consulting and training Meridian 500 companies, small and midsize companies as well as individuals looking to improve their international business skills.</p>
    <p>There is significant evidence that cross-cultural training and knowledge lead to more successful international business relationships and they are key to success for mergers and acquisitions as well as joint ventures. “Your Success Drives our Success.” It is our goal to be a long term partner in your international growth strategies and development. Contact us today to get started.</p>
    <hr class="rule">
    <p>Offices in Harlow Bay, Eastmere, Sandcroft, Valmora Heights, Oreno and Port Calder.</p>
    <hr class="rule">
    <div class="brand"><span class="brand__mark"></span>BRENVALE ADVISORY</div>
    <dl class="contact">
      <dt>Address</dt>
      <dd>418 Larkspur Ave. Suite 120<br>Austin, TX 78701</dd>
      <dt>Phone</dt>
      <dd>(512) 555-0147</dd>
      <dt>Email</dt>
      <dd>info@brenvaleadvisory.com</dd>
      <dt>Web</dt>
      <dd class="web">brenvaleadvisory.com</dd>
      <dd class="copyright">©Northfield Partners, LLC.</dd>
    </dl>
  </section>
</main>
</body>
</html>
```